Process Graphic for website

We would like to design a graphic that shows our internal process for scanning our customer records. Our process is listed in order below:
Transport Documents
Inventory Records
Document Preparation
Scan Documents
AI & Data Extraction
Quality Control
Deliver Documents
Records Retention or Destruction

Our customers need to know that we have a clear defined process for scanning records and it needs to visually demonstrate that in a simple way. I have attached our logo as these are the colors of our new website so whatever colors you chose should match our site.

```html
<!DOCTYPE html>
<html lang="en">
<head>
<meta charset="utf-8">
<title>Document Scanning Process</title>
<link href="https://fonts.googleapis.com/css2?family=Jost:wght@500&display=swap" rel="stylesheet">
<style>
  :root {
    --paper: #ffffff;
    --ink: #141414;
    --navy: #2e3192;
    --gold: #c9960c;
    --trail: #f1f1f3;
  }
  html, body {
    margin: 0;
    width: 1200px;
    height: 834px;
    overflow: hidden;
    background: var(--paper);
  }
  .process {
    position: relative;
    width: 1200px;
    height: 834px;
    font-family: "Jost", "Futura", sans-serif;
    font-weight: 500;
    color: var(--ink);
  }
  .process-graphics {
    position: absolute;
    inset: 0;
  }
  .step-label {
    position: absolute;
    margin: 0;
    font-size: 38px;
    line-height: 33px;
    font-weight: 500;
    letter-spacing: 0.2px;
    white-space: nowrap;
  }
  .icon { fill: none; stroke: var(--navy); stroke-width: 4; stroke-linejoin: round; stroke-linecap: round; }
  .icon-fill { fill: var(--navy); }
  .arrow { fill: var(--gold); }
  .trail { fill: none; stroke: var(--trail); stroke-width: 5; }
</style>
</head>
<body>
<main class="process" aria-label="Document scanning process">
  <svg class="process-graphics" width="1200" height="834" viewBox="0 0 1200 834" aria-hidden="true">
    <!-- connector trail -->
    <path class="trail" d="M190 250 H830 C960 250 930 330 900 360 C880 380 860 420 220 420 C100 420 100 590 230 590 H820"/>

    <!-- transport: document + truck -->
    <g class="icon">
      <path d="M98 240 V212 H134 L144 222 V262"/>
      <path d="M106 224 H126 M106 234 H136 M106 244 H136 M106 254 H136"/>
      <rect x="92" y="262" width="82" height="14"/>
      <path d="M150 238 H176 L188 256 V276 H174"/>
      <path d="M162 244 V256 H182"/>
      <circle cx="113" cy="281" r="9"/>
      <circle cx="168" cy="281" r="9"/>
    </g>

    <!-- inventory: document with check -->
    <g class="icon">
      <path d="M506 250 V214 H550 L565 229 V290 H520"/>
      <path d="M550 214 V229 H565"/>
      <path d="M520 238 H552 M530 254 H552 M530 270 H552"/>
      <circle cx="508" cy="272" r="17"/>
      <path d="M499 272 L506 279 L518 265"/>
    </g>

    <!-- document preparation: stacked pages with clip -->
    <g class="icon">
      <rect x="834" y="216" width="50" height="62"/>
      <path d="M884 222 H892 V290 H842 V278"/>
      <path d="M892 230 H896 V294"/>
      <path d="M844 222 V238 H860"/>
      <path d="M846 250 H872 M846 258 H876 M846 266 H876 M866 226 H876 M866 234 H876 M876 242 V246"/>
      <path d="M840 216 V228 A4 4 0 0 0 848 228 V220"/>
    </g>

    <!-- scan: document in frame -->
    <g class="icon">
      <path d="M772 386 V374 H784 M836 374 H848 V386 M772 452 V464 H784 M836 464 H848 V452"/>
      <path d="M790 434 V386 H822 L834 398 V434"/>
      <path d="M822 386 V398 H834"/>
      <path d="M770 428 H850"/>
      <rect x="790" y="428" width="44" height="26"/>
      <path d="M798 410 H814 M798 418 H826 M798 440 H826 M798 447 H826"/>
    </g>

    <!-- AI & data extraction: monitor with document and sync -->
    <g class="icon">
      <rect x="440" y="380" width="70" height="62"/>
      <path d="M440 428 H510 M466 442 L462 456 M484 442 L488 456 M456 456 H494"/>
      <path d="M456 428 V378 H490 L498 386 V428"/>
      <path d="M466 394 A8 8 0 0 1 482 392 M484 400 A8 8 0 0 1 468 402"/>
      <path d="M462 412 H492 M462 420 H486"/>
      <path d="M446 390 V396 M446 404 V410"/>
    </g>

    <!-- quality control: document with award seal -->
    <g class="icon">
      <path d="M196 444 H144 V376 H190 L200 386 V400"/>
      <path d="M190 376 V386 H200"/>
      <path d="M152 390 H172 M152 400 H188 M152 410 H184 M152 420 H178 M152 430 H182"/>
      <circle cx="207" cy="430" r="19"/>
      <circle cx="207" cy="430" r="12"/>
      <path d="M201 430 L205 434 L213 425"/>
      <path d="M196 446 L191 461 L199 458 L203 463 L206 449 M218 446 L222 461 L214 458 L210 463"/>
    </g>

    <!-- records retention: document with x badge -->
    <g class="icon">
      <path d="M246 580 V552 H290 L302 564 V620 H262"/>
      <path d="M290 552 V564 H302"/>
      <path d="M262 576 H292 M270 592 H292 M270 606 H292"/>
      <circle cx="248" cy="604" r="16"/>
      <path d="M242 598 L254 610 M254 598 L242 610"/>
    </g>

    <!-- deliver: cloud with document -->
    <g class="icon">
      <path d="M738 606 H720 A16 16 0 0 1 716 575 A24 24 0 0 1 760 560 A20 20 0 0 1 790 586 A16 16 0 0 1 776 606 H770"/>
      <path d="M734 626 V586 H760 L770 596 V626 Z"/>
      <path d="M760 586 V596 H770"/>
      <path d="M742 604 H760 M742 614 H760"/>
    </g>

    <!-- direction arrows -->
    <polygon class="arrow" points="426,237 448,248 426,259"/>
    <polygon class="arrow" points="772,242 794,253 772,264"/>
    <polygon class="arrow" points="894,336 918,336 906,358"/>
    <polygon class="arrow" points="738,417 716,428 738,439"/>
    <polygon class="arrow" points="412,417 390,428 412,439"/>
    <polygon class="arrow" points="102,540 122,522 124,546"/>
    <polygon class="arrow" points="646,581 668,592 646,603"/>
  </svg>

  <p class="step-label" style="left:206px; top:216px;">Transport<br>Documents</p>
  <p class="step-label" style="left:582px; top:216px;">Inventory<br>Records</p>
  <p class="step-label" style="left:914px; top:216px;">Document<br>Preparation</p>
  <p class="step-label" style="left:872px; top:382px;">Scan<br>Documents</p>
  <p class="step-label" style="left:528px; top:382px;">AI &amp; Data<br>Extraction</p>
  <p class="step-label" style="left:237px; top:382px;">Quality<br>Control</p>
  <p class="step-label" style="left:319px; top:548px;">Records Retention<br>or Destruction</p>
  <p class="step-label" style="left:804px; top:548px;">Deliver<br>Documents</p>
</main>
</body>
</html>
```